Sales Leaning Business Card for a Restoration Company - Construction Company
Halvorn Renewal, Inc.
Professional
Benedict L Marlowe Jr
President
318 Fenwirk Ave
Lake Dallas, TX 75065
bmarlowe@hnwok-example.com
www.hnwok-example.com
I would like the card to be more of a salesman's card. Should look professional but lean a bit more towards a sales tool.
24 Hour emergency Services
Water & Fire Damage Restoration
Water Removal and Structural Drying
Storm Damage
Hail / Roofing Damage
Post Mitigation Reconstruction
QNV Accredited
PSTAW Certified

```html
<!DOCTYPE html>
<html lang="en">
<head>
<meta charset="utf-8">
<title>Halvorn Renewal, Inc. — Stationery Set</title>
<link href="https://fonts.googleapis.com/css2?family=Montserrat:wght@400;500;600;700&display=swap" rel="stylesheet">
<style>
  :root {
    --bg: #eceeef;
    --paper: #ffffff;
    --brand-blue: #1e5683;
    --brand-deep: #143b5e;
    --brand-light: #2f6f9f;
    --ink: #1c3c5c;
    --grey: #6d7378;
    --rule: #4a4f54;
    --faint: #e9eef2;
  }
  * { box-sizing: border-box; margin: 0; padding: 0; }
  html, body { width: 1200px; height: 936px; overflow: hidden; }
  body {
    background: var(--bg);
    font-family: "Montserrat", Arial, sans-serif;
    color: var(--ink);
    position: relative;
  }
  .piece { position: absolute; background: var(--paper); overflow: hidden; }

  /* brand lockup */
  .lockup { display: flex; align-items: center; gap: 8px; }
  .lockup .mark { border-radius: 50%; background: var(--brand-blue); flex: none; }
  .lockup .name { color: var(--ink); font-weight: 600; line-height: 1.05; letter-spacing: 0.06em; }
  .lockup .name span { display: block; }

  /* letterhead */
  .letterhead { left: 183px; top: 46px; width: 419px; height: 568px; }
  .letterhead .lockup { position: absolute; left: 30px; top: 52px; }
  .letterhead .mark { width: 30px; height: 30px; }
  .letterhead .name span:first-child { font-size: 20px; }
  .letterhead .name span:last-child { font-size: 8.5px; letter-spacing: 0.12em; }
  .letterhead .contact {
    position: absolute; left: 225px; top: 50px;
    font-size: 6px; line-height: 9.5px; color: var(--grey);
    list-style: none;
  }
  .letterhead .contact li::before {
    content: ""; display: inline-block; width: 4px; height: 4px;
    background: var(--brand-blue); border-radius: 50%; margin-right: 4px; vertical-align: middle;
  }
  .letterhead .watermark {
    position: absolute; left: 153px; top: 244px; width: 112px; height: 112px;
    border-radius: 50%; background: var(--faint);
  }

  /* presentation folder */
  .folder {
    left: 634px; top: 46px; width: 457px; height: 568px;
    background: radial-gradient(ellipse at 50% 45%, var(--brand-light) 0%, var(--brand-blue) 45%, var(--brand-deep) 100%);
  }
  .folder .band {
    position: absolute; left: 0; top: 188px; width: 100%; height: 193px;
    background: var(--paper);
    border-top: 6px solid var(--rule); border-bottom: 6px solid var(--rule);
    display: flex; justify-content: center; align-items: center;
  }
  .folder .mark { width: 62px; height: 62px; }
  .folder .lockup { gap: 14px; }
  .folder .name span:first-child { font-size: 40px; }
  .folder .name span:last-child { font-size: 16px; letter-spacing: 0.12em; }

  /* business card front */
  .card-front { left: 43px; top: 655px; width: 200px; height: 112px; }
  .card-front .lockup { position: absolute; left: 10px; top: 10px; gap: 5px; }
  .card-front .mark { width: 14px; height: 14px; }
  .card-front .name span:first-child { font-size: 10px; }
  .card-front .name span:last-child { font-size: 4.5px; }
  .card-front .person { position: absolute; left: 10px; top: 46px; font-size: 5px; line-height: 7px; color: var(--grey); }
  .card-front .person strong { color: var(--ink); font-weight: 600; display: block; }
  .card-front .details { position: absolute; left: 108px; top: 42px; font-size: 4.5px; line-height: 7px; color: var(--grey); list-style: none; }
  .card-front .band {
    position: absolute; left: 0; bottom: 0; width: 100%; height: 12px;
    background: var(--brand-blue); color: var(--paper);
    font-size: 5px; font-weight: 600; letter-spacing: 0.14em;
    display: flex; align-items: center; justify-content: center;
  }

  /* business card back: services and credentials */
  .card-back { left: 43px; top: 781px; width: 200px; height: 107px; }
  .card-back .mark {
    position: absolute; left: 12px; top: 33px;
    width: 34px; height: 34px; border-radius: 50%; background: var(--brand-blue);
  }
  .card-back .services { position: absolute; left: 58px; top: 9px; width: 134px; }
  .card-back .services h2 {
    font-size: 5.5px; font-weight: 700; color: var(--brand-blue);
    letter-spacing: 0.08em; margin-bottom: 3px;
  }
  .card-back .services ul { list-style: none; font-size: 4.6px; line-height: 7px; color: var(--grey); }
  .card-back .services li::before {
    content: ""; display: inline-block; width: 2.5px; height: 2.5px;
    background: var(--brand-blue); border-radius: 50%; margin-right: 3px; vertical-align: middle;
  }
  .card-back .credentials {
    position: absolute; left: 58px; top: 84px; display: flex; gap: 10px;
    font-size: 4.6px; font-weight: 600; color: var(--ink);
  }
  .card-back .credentials span { display: flex; align-items: center; gap: 3px; }
  .card-back .credentials i {
    display: inline-block; width: 9px; height: 9px; border-radius: 2px; background: var(--rule);
  }

  /* envelopes */
  .envelope-front { left: 264px; top: 657px; width: 360px; height: 223px; }
  .envelope-front .lockup { position: absolute; left: 18px; top: 40px; }
  .envelope-front .mark { width: 24px; height: 24px; }
  .envelope-front .name span:first-child { font-size: 16px; }
  .envelope-front .name span:last-child { font-size: 7px; letter-spacing: 0.12em; }
  .envelope-front .return { position: absolute; left: 18px; top: 88px; font-size: 5.5px; color: var(--grey); letter-spacing: 0.05em; }

  .envelope-back { left: 665px; top: 657px; width: 467px; height: 223px; }
  .envelope-back svg { position: absolute; left: 0; top: 0; }
  .envelope-back .web {
    position: absolute; left: 0; top: 26px; width: 100%; text-align: center;
    color: var(--paper); font-size: 7px; letter-spacing: 0.45em; font-weight: 500;
  }
</style>
</head>
<body>

<section class="piece letterhead" aria-label="Letterhead">
  <div class="lockup">
    <div class="mark"></div>
    <div class="name"><span>HALVORN</span><span>RENEWAL</span></div>
  </div>
  <ul class="contact">
    <li>318 Fenwirk Ave</li>
    <li>Lake Dallas, TX 75065</li>
    <li>Tel 940 555 0142</li>
    <li>Fax 940 555 0143</li>
    <li>bmarlowe@hnwok-example.com</li>
    <li>www.hnwok-example.com</li>
  </ul>
  <div class="watermark"></div>
</section>

<section class="piece folder" aria-label="Presentation folder">
  <div class="band">
    <div class="lockup">
      <div class="mark"></div>
      <div class="name"><span>HALVORN</span><span>RENEWAL</span></div>
    </div>
  </div>
</section>

<section class="piece card-front" aria-label="Business card front">
  <div class="lockup">
    <div class="mark"></div>
    <div class="name"><span>HALVORN</span><span>RENEWAL</span></div>
  </div>
  <div class="person"><strong>Benedict L Marlowe Jr</strong>President</div>
  <ul class="details">
    <li>Cell 940 555 0144</li>
    <li>318 Fenwirk Ave, Lake Dallas, TX 75065</li>
    <li>bmarlowe@hnwok-example.com</li>
    <li>www.hnwok-example.com</li>
  </ul>
  <div class="band">24 HOUR EMERGENCY SERVICES</div>
</section>

<section class="piece card-back" aria-label="Business card back">
  <div class="mark"></div>
  <div class="services">
    <h2>24 HOUR EMERGENCY SERVICES</h2>
    <ul>
      <li>Water &amp; Fire Damage Restoration</li>
      <li>Water Removal and Structural Drying</li>
      <li>Storm Damage</li>
      <li>Hail / Roofing Damage</li>
      <li>Post Mitigation Reconstruction</li>
    </ul>
  </div>
  <div class="credentials">
    <span><i></i>QNV Accredited</span>
    <span><i></i>PSTAW Certified</span>
  </div>
</section>

<section class="piece envelope-front" aria-label="Envelope front">
  <div class="lockup">
    <div class="mark"></div>
    <div class="name"><span>HALVORN</span><span>RENEWAL</span></div>
  </div>
  <p class="return">318 Fenwirk Ave, Lake Dallas, TX 75065</p>
</section>

<section class="piece envelope-back" aria-label="Envelope back">
  <svg width="467" height="223" viewBox="0 0 467 223" aria-hidden="true">
    <defs>
      <linearGradient id="flapFill" x1="0" y1="0" x2="1" y2="0">
        <stop offset="0" stop-color="#143b5e"/>
        <stop offset="0.5" stop-color="#2f6f9f"/>
        <stop offset="1" stop-color="#143b5e"/>
      </linearGradient>
    </defs>
    <polygon points="0,0 467,0 467,88 233,112 0,88" fill="url(#flapFill)"/>
    <polyline points="0,88 233,112 467,88" fill="none" stroke="#d9dde0" stroke-width="1"/>
  </svg>
  <p class="web">WWW.HNWOK-EXAMPLE.COM</p>
</section>

</body>
</html>
```